Business card and stationery design

Harbour & Summit Planners is a leading event and conference design and management company.
Please view harbourandsummit.com.au

The business cards needs to convey:
- professionalism and competency
- exclusivity
- memorable experiences and quality

The business card needs to have the following aspects:
- double sided
- Full colour CMYK
- Printed on either high gloss matt card (designer to recommend)

For the business stationery we require:
- Letterhead with top banner and bottom footer
- A thank you card design
- a with compliments slip design
- a MS powerpoint and MS publisher client presentation slide design which includes cover page and then a standard presentation page
(Note- we do NOT require an envelope design- who sends letters these days!)

The company image is using the key colours of gold, silver and black.
A black background to the business card has been used before and is preferred although we are open to options.

Target Market(s)

High end corporations and businesses that require their events and conferences to be exceptionally well designed and managed

Industry/Entity Type

Business

Contact Information for Business Card

FRONT:

Darcy Whitlam
- Event and Conference Specialist

Mobile- +61 (0) 491 362 047
Office- 1300 586 917
darcyw@harbourandsummit.com.au

Web- harbourandsummit.com.au

BACK:

- Event and

Font styles to use
Other font styles liked:
• The logo designer used Trajan Pro Bold 3 for the font text in the logo

Requirements
Must have
• Amazing design of the following:
• - business card (double sided)
• - letterhead
• - client thank you card
• - powerpoint and publisher client presentation design files

```html
<!DOCTYPE html>
<html lang="en">
<head>
<meta charset="utf-8">
<title>Harbour &amp; Summit Planners – Business Card</title>
<link rel="stylesheet" href="https://fonts.googleapis.com/css2?family=Montserrat:wght@300;400;700&family=Cinzel:wght@400;700&display=swap">
<style>
  :root {
    --backdrop: #2b2622;
    --card-black: #0b0b0b;
    --card-sheen: #1c1c1c;
    --gold: #d2ac5e;
    --gold-light: #ecd398;
    --white: #f2f2f2;
    --grey: #cfcfcf;
  }
  * { margin: 0; padding: 0; box-sizing: border-box; }
  html, body {
    width: 1200px; height: 913px; overflow: hidden;
    background: var(--backdrop);
  }
  .canvas {
    position: relative; width: 1200px; height: 913px;
    display: flex; align-items: center; justify-content: center; gap: 50px;
  }
  .card {
    position: relative; width: 540px; height: 310px;
    border-radius: 16px; overflow: hidden;
    background: linear-gradient(135deg, var(--card-sheen) 0%, var(--card-black) 55%, #050505 100%);
    box-shadow: 0 18px 40px rgba(0,0,0,.55);
    font-family: "Montserrat", sans-serif; color: var(--white);
  }
  /* front */
  .card-front .edge-band {
    position: absolute; left: 24px; top: 0; bottom: 0; width: 22px;
    background: linear-gradient(90deg, #b68d3f, var(--gold-light), var(--gold));
  }
  .brand-lockup { position: absolute; left: 78px; top: 54px; width: 300px; }
  .brand-name {
    font-family: "Montserrat", sans-serif; font-weight: 300;
    font-size: 23px; line-height: 1.2; color: var(--white); letter-spacing: .3px;
  }
  .brand-rule { height: 2px; background: var(--gold); margin-top: 12px; width: 290px; }
  .contact-block {
    position: absolute; right: 28px; top: 126px; text-align: right;
  }
  .person-name { font-weight: 700; font-size: 19px; color: var(--gold); }
  .person-role { font-size: 10.5px; color: var(--white); margin-top: 2px; margin-bottom: 10px; }
  .contact-line {
    display: flex; justify-content: flex-end; align-items: center; gap: 7px;
    font-size: 11px; line-height: 17px; color: var(--grey); font-weight: 300;
  }
  .contact-line svg { width: 10px; height: 10px; flex: none; }
  .contact-line.no-icon { padding-right: 17px; }
  /* back */
  .card-back { display: flex; flex-direction: column; align-items: center; justify-content: center; }
  .back-name {
    font-family: "Montserrat", sans-serif; font-weight: 700;
    font-size: 34px; color: var(--gold); letter-spacing: .5px;
  }
  .back-web {
    margin-top: 26px; font-family: "Cinzel", serif; font-size: 15px; letter-spacing: 1.5px;
    color: var(--white);
  }
  .back-web .accent { color: var(--gold); }
</style>
</head>
<body>
<main class="canvas">
  <section class="card card-front" aria-label="Business card front">
    <div class="edge-band"></div>
    <div class="brand-lockup">
      <div class="brand-name">Harbour &amp; Summit Planners</div>
      <div class="brand-rule"></div>
    </div>
    <div class="contact-block">
      <div class="person-name">Darcy Whitlam</div>
      <div class="person-role">Event and Conference Specialist</div>
      <div class="contact-line">1300 586 917
        <svg viewBox="0 0 10 10"><path d="M2 1 L4 1 L4.6 3 L3.5 3.8 Q4.5 5.8 6.2 6.5 L7 5.4 L9 6 L9 8 Q5 9 2 5.5 Q1 3.5 2 1Z" fill="var(--gold)"/></svg>
      </div>
      <div class="contact-line">+61 (0) 491 362 047
        <svg viewBox="0 0 10 10"><rect x="2.5" y="0.5" width="5" height="9" rx="1" fill="none" stroke="var(--gold)" stroke-width="1"/><circle cx="5" cy="8" r=".6" fill="var(--gold)"/></svg>
      </div>
      <div class="contact-line">darcyw@harbourandsummit.com.au
        <svg viewBox="0 0 10 10"><rect x="0.5" y="2" width="9" height="6" fill="var(--gold)"/><path d="M0.5 2 L5 5.5 L9.5 2" fill="none" stroke="#000" stroke-width=".8"/></svg>
      </div>
      <div class="contact-line">www.harbourandsummit.com.au
        <svg viewBox="0 0 10 10"><circle cx="5" cy="5" r="4.3" fill="var(--gold)"/><path d="M0.7 5 H9.3 M5 0.7 Q2.5 5 5 9.3 M5 0.7 Q7.5 5 5 9.3" fill="none" stroke="#000" stroke-width=".6"/></svg>
      </div>
    </div>
  </section>

  <section class="card card-back" aria-label="Business card back">
    <div class="back-name">Harbour &amp; Summit</div>
    <div class="back-web"><span class="accent">www.</span>harbourandsummit<span class="accent">.com.au</span></div>
  </section>
</main>
</body>
</html>
```